Voltara Solutions Ltd - Project for new electric vehicle charging company

Please use Voltara Solutions Ltd logo & artwork instead of Brightwell.

We would like to produce a leaflet to advertise our electric vehicle charging company to build a reputation and workflow in the local area.

We would like to use the attached logo and maintain the colour palette of the of the logo to be simple, modern and effective.

I have over 15 years experience in the electrical industry and have direct access to the latest technology in electric vehicle charging.

All quotes to remain fixed costs subject to survey of the property and maintenance options can be available.

We can also offer further remedial works to any property through our sister company Brightwell Solutions Ltd.

Target Market(s)

Domestic / commercial customers

Requirements
Must have
• Voltara Solutions Ltd logo and colour palette.
Should not have
• Brightwell logo, Email or website address.

```html
<!DOCTYPE html>
<html lang="en">
<head>
<meta charset="utf-8">
<title>Voltara Solutions Ltd – Leaflet</title>
<link rel="stylesheet" href="https://fonts.googleapis.com/css2?family=Montserrat:wght@500;600;800&family=Arimo&display=swap">
<style>
  :root {
    --page-bg: #eef2f1;
    --forest: #1c5d4e;
    --forest-light: #2f8a76;
    --teal: #10b7a2;
    --teal-deep: #0a907d;
    --teal-text: #0f8d7b;
    --grey-text: #8a8a8a;
    --paper: #ffffff;
    --paper-shade: #eceeef;
    --white: #ffffff;
  }
  html, body {
    margin: 0;
    width: 1200px;
    height: 1200px;
    overflow: hidden;
    background: var(--page-bg);
  }
  .leaflet {
    position: absolute;
    left: 190px;
    top: 20px;
    width: 820px;
    height: 1160px;
    display: block;
  }
  .brand-name { font-family: "Montserrat", sans-serif; font-weight: 500; fill: var(--white); }
  .headline { font-family: "Montserrat", sans-serif; font-weight: 800; fill: var(--white); }
  .subline { font-family: "Montserrat", sans-serif; font-weight: 600; fill: var(--white); }
  .section-title { font-family: "Montserrat", sans-serif; font-weight: 800; fill: var(--teal-text); }
  .intro { font-family: "Montserrat", sans-serif; font-weight: 500; fill: var(--grey-text); }
  .service-label { font-family: "Montserrat", sans-serif; font-weight: 800; fill: var(--teal-text); }
  .contact { font-family: "Arimo", sans-serif; fill: var(--white); }
</style>
</head>
<body>
<svg class="leaflet" viewBox="0 0 820 1160" xmlns="http://www.w3.org/2000/svg">
  <defs>
    <linearGradient id="paperFill" x1="0" y1="0" x2="1" y2="1">
      <stop offset="0" stop-color="var(--paper)"/>
      <stop offset="1" stop-color="var(--paper-shade)"/>
    </linearGradient>
    <linearGradient id="heroFill" x1="0" y1="0" x2="1" y2="0.6">
      <stop offset="0" stop-color="#1b5a4b"/>
      <stop offset="0.55" stop-color="#235f4f"/>
      <stop offset="1" stop-color="#5aa999"/>
    </linearGradient>
    <linearGradient id="photoCharger" x1="0" y1="0" x2="1" y2="1">
      <stop offset="0" stop-color="#d9dcdc"/>
      <stop offset="0.5" stop-color="#3a3d3f"/>
      <stop offset="1" stop-color="#8d8f90"/>
    </linearGradient>
    <linearGradient id="photoDriver" x1="0" y1="0" x2="1" y2="1">
      <stop offset="0" stop-color="#5b5e63"/>
      <stop offset="0.45" stop-color="#d8d6d2"/>
      <stop offset="1" stop-color="#b9b4ad"/>
    </linearGradient>
    <linearGradient id="photoStreet" x1="0" y1="0" x2="0" y2="1">
      <stop offset="0" stop-color="#7c8a6a"/>
      <stop offset="0.55" stop-color="#eef0f1"/>
      <stop offset="1" stop-color="#5a5a4f"/>
    </linearGradient>
    <clipPath id="heroClip">
      <path d="M0 0 H820 V330 Q410 624 0 330 Z"/>
    </clipPath>
  </defs>

  <!-- paper -->
  <rect class="paper" x="0" y="0" width="820" height="1160" fill="url(#paperFill)"/>

  <!-- soft halo behind header -->
  <path class="header-halo" d="M0 0 H820 V430 Q410 590 0 430 Z" fill="#e9ebeb"/>

  <!-- header with photo area -->
  <g class="hero" clip-path="url(#heroClip)">
    <rect role="img" aria-label="Photo of an electric car plugged into a wall charging unit, tinted dark green" x="0" y="0" width="820" height="640" fill="url(#heroFill)"/>
  </g>

  <!-- brand -->
  <g class="brand">
    <circle cx="231" cy="87" r="26" fill="var(--white)"/>
    <text class="brand-name" x="269" y="97" font-size="28">Voltara Solutions Ltd</text>
  </g>

  <!-- headline -->
  <text class="headline" x="410" y="228" font-size="69" text-anchor="middle">15 Years</text>
  <text class="headline" x="410" y="297" font-size="69" text-anchor="middle">Experience</text>
  <text class="subline" x="410" y="361" font-size="35" text-anchor="middle">in the electrical industry</text>

  <!-- photo circles -->
  <g class="photo-circle">
    <circle cx="226" cy="541" r="102" fill="var(--teal)"/>
    <circle role="img" aria-label="Photo of a charging cable hanging on a public charging post" cx="226" cy="541" r="88" fill="url(#photoCharger)"/>
  </g>
  <g class="photo-circle">
    <circle cx="599" cy="541" r="102" fill="var(--teal)"/>
    <circle role="img" aria-label="Photo of a white electric car charging at a street charger" cx="599" cy="541" r="88" fill="url(#photoStreet)"/>
  </g>
  <g class="photo-circle photo-circle--main">
    <circle cx="412" cy="541" r="147" fill="var(--teal)"/>
    <circle role="img" aria-label="Photo of a driver charging a white electric car" cx="412" cy="541" r="125" fill="url(#photoDriver)"/>
  </g>

  <!-- what we offer -->
  <text class="section-title" x="410" y="751" font-size="34" text-anchor="middle">What We Offer</text>
  <text class="intro" x="410" y="795" font-size="21" text-anchor="middle">Proin ac leo quis odio ullamcorper egestas. Nunc dictum</text>
  <text class="intro" x="410" y="827" font-size="21" text-anchor="middle">ante eget aliquam aliquet. Donec fermentum imperdiet.</text>

  <!-- services -->
  <g class="service" transform="translate(111 890)">
    <circle r="33" fill="var(--teal-deep)"/>
    <g fill="none" stroke="var(--white)" stroke-width="1.8" stroke-linejoin="round" stroke-linecap="round">
      <rect x="-14" y="-18" width="20" height="32" rx="2"/>
      <path d="M-4 -12 l-4 7 h5 l-4 7"/>
      <path d="M6 -8 h6 v14 a3 3 0 0 1 -6 0"/>
    </g>
  </g>
  <text class="service-label" x="111" y="955" font-size="20" text-anchor="middle">Aenean at</text>
  <text class="service-label" x="111" y="982" font-size="20" text-anchor="middle">laoreet tellus</text>

  <g class="service" transform="translate(302 890)">
    <circle r="33" fill="var(--teal-deep)"/>
    <g fill="none" stroke="var(--white)" stroke-width="1.8" stroke-linejoin="round" stroke-linecap="round">
      <rect x="-11" y="-19" width="18" height="32" rx="2"/>
      <rect x="-7" y="-15" width="10" height="9"/>
      <path d="M-1 -3 l-3 5 h4 l-3 5"/>
      <path d="M7 8 h5 v6"/>
    </g>
  </g>
  <text class="service-label" x="302" y="955" font-size="20" text-anchor="middle">Duis vulput</text>
  <text class="service-label" x="302" y="982" font-size="20" text-anchor="middle">sed odio quis</text>

  <g class="service" transform="translate(497 890)">
    <circle r="33" fill="var(--teal-deep)"/>
    <g fill="none" stroke="var(--white)" stroke-width="1.8" stroke-linejoin="round" stroke-linecap="round">
      <rect x="-13" y="-19" width="18" height="34" rx="2"/>
      <rect x="-9" y="-15" width="10" height="7"/>
      <path d="M-3 -3 l-4 7 h5 l-4 7"/>
      <path d="M5 -2 l6 -5 l5 8 l-5 3"/>
    </g>
  </g>
  <text class="service-label" x="497" y="955" font-size="20" text-anchor="middle">Praesent gra</text>
  <text class="service-label" x="497" y="982" font-size="20" text-anchor="middle">Vida tincidunt</text>

  <g class="service" transform="translate(697 890)">
    <circle r="33" fill="var(--teal-deep)"/>
    <g fill="none" stroke="var(--white)" stroke-width="1.8" stroke-linejoin="round" stroke-linecap="round">
      <path d="M-18 -14 h36"/>
      <circle cx="0" cy="-6" r="5"/>
      <rect x="-17" y="2" width="16" height="12" rx="2"/>
      <rect x="4" y="-2" width="12" height="16" rx="1"/>
    </g>
  </g>
  <text class="service-label" x="697" y="955" font-size="20" text-anchor="middle">Curabitur in</text>
  <text class="service-label" x="697" y="982" font-size="20" text-anchor="middle">leo vitae massa</text>

  <!-- footer -->
  <path class="footer-edge" d="M0 1066 Q410 956 820 1066 V1160 H0 Z" fill="var(--teal-deep)"/>
  <path class="footer" d="M0 1073 Q410 965 820 1073 V1160 H0 Z" fill="var(--teal)"/>

  <g class="contact-row">
    <circle cx="59" cy="1100" r="12" fill="var(--white)"/>
    <path d="M53 1094 q1 -2 3 -1 l2 3 q0 2 -2 2 q1 3 4 4 q0 -2 2 -2 l3 2 q1 2 -1 3 q-6 1 -11 -11 z" fill="var(--teal)"/>
    <text class="contact" x="81" y="1106" font-size="15.5">0121-555-0147</text>
    <text class="contact" x="194" y="1106" font-size="15.5">|</text>

    <circle cx="220" cy="1100" r="12" fill="var(--white)"/>
    <rect x="213" y="1095" width="14" height="10" rx="1" fill="none" stroke="var(--teal)" stroke-width="1.5"/>
    <path d="M213 1096 l7 5 l7 -5" fill="none" stroke="var(--teal)" stroke-width="1.5"/>
    <text class="contact" x="243" y="1106" font-size="15.5">enquiries@voltara-solutions.com</text>
    <text class="contact" x="494" y="1106" font-size="15.5">|</text>

    <circle cx="517" cy="1100" r="12" fill="var(--white)"/>
    <g fill="none" stroke="var(--teal)" stroke-width="1.3">
      <circle cx="517" cy="1100" r="7"/>
      <ellipse cx="517" cy="1100" rx="3" ry="7"/>
      <path d="M510 1100 h14"/>
    </g>
    <text class="contact" x="540" y="1106" font-size="15.5">www.voltara-solutions.co.uk</text>
  </g>
</svg>
</body>
</html>
```